Item Change Management Brochure / FAQ

Create a very stunning, infographic based brochure around a process Birch Supply Company calls "Item Change Management". The audience for the brochure are Birch Supply retail store owners and operators who need to be amazed by the program. This brochure is to make it easy for Birch Supply store owners to understand the program, its benefits, and the process behind it. Here are some important notes about the brochure:

* Must all fit content on 2 pages - a front and back side - 8-1/2x11"
* Font must be no smaller than size 11 Calibri. Calibri does NOT have to be used but just want to level set the size.
* Use Birch Supply colors (red, black, and white).
* Graphics and design must be super amazing to look at
* The document Word titled "Item Change Management" has most of the content needed. Use the provided photos as you see fit.
* Important: I would like the Excel file to appear in the 2-page brochure. The Word document titled Item Change Management Sales Floor and Back Office Actions is the legend for the Excel file (rows 8,9,16, and 17 of Excel file).

Target Market(s)

Birch Supply store owners and operators

Industry/Entity Type

Retail

Font styles to use
Sans Serif

Colors
EB3D1F
EC4F4E
F09395
F8D3D4
FCEDEE

Requirements
Must have
• * Unique and look extremely creative, 8-1/2x11", font size that is readable to average eye, Birch Supply colors, all content provided (images provided are optional), infographics where possible, the chart must look incredible.
Should not have
• Boring, too standard, traditional.

```html
<!DOCTYPE html>
<html lang="en">
<head>
<meta charset="utf-8">
<title>Item Change Management FAQ</title>
<link href="https://fonts.googleapis.com/css2?family=Open+Sans:wght@400;600;700&family=Poppins:wght@400;500;600&family=Roboto:wght@700;900&display=swap" rel="stylesheet">
<style>
:root{
  --red:#e31b3b;
  --red-soft:#f09395;
  --black:#1d1d1d;
  --ink:#222;
  --stripe:#e9e9ea;
  --white:#fff;
}
*{box-sizing:border-box;margin:0;padding:0}
html,body{width:888px;height:1200px;overflow:hidden;background:var(--white)}
.page{position:relative;width:888px;height:1200px;overflow:hidden;background:var(--white);font-family:"Open Sans",sans-serif;color:var(--ink)}
.brand{position:absolute;left:59px;top:40px;display:flex;align-items:center;gap:12px}
.brand-name{font-family:"Open Sans",sans-serif;font-weight:700;font-size:20px;color:var(--red);letter-spacing:-.3px}
.brand-divider{width:1px;height:34px;background:#ccc}
.brand-unit{font-family:"Poppins",sans-serif;line-height:1}
.brand-unit .top{display:block;font-size:13px;font-weight:600;color:#555;letter-spacing:.5px}
.brand-unit .bottom{display:block;font-size:19px;font-weight:600;color:var(--red);letter-spacing:.6px}
.hero{position:absolute;left:0;top:0}
.title-band{position:absolute;left:0;top:121px;width:888px;height:84px;background:var(--black);display:flex;align-items:center;justify-content:center}
.title-band h1{font-family:"Roboto",sans-serif;font-weight:900;font-size:23.5px;color:var(--white);letter-spacing:.1px;white-space:nowrap}
.title-band h1 span{color:var(--red)}
.faq{position:absolute}
.faq .num{position:absolute;left:0;top:0;width:38px;height:38px;border-radius:50%;background:var(--black);border:2px solid var(--white);box-shadow:0 0 0 2px var(--red);color:var(--white);font-family:"Roboto",sans-serif;font-weight:900;font-size:17px;display:flex;align-items:center;justify-content:center}
.faq h2{font-family:"Open Sans",sans-serif;font-weight:600;font-size:12.6px;line-height:17.5px;color:var(--red);letter-spacing:.2px;text-transform:uppercase}
.faq p{font-size:9.4px;line-height:14.6px;margin-top:5px;color:#2a2a2a}
.faq p.just{text-align:justify}
.faq h2.big{font-size:15px;line-height:21px}
.table-title{position:absolute;left:59px;top:909px;display:flex;align-items:center;gap:14px}
.table-title .num{position:relative}
.fields{position:absolute;left:59px;top:963px;width:772px;height:135px;border:2px solid var(--red);border-radius:14px;overflow:hidden;display:grid;grid-template-columns:186px 147px 171px 127px 1fr}
.fields .col{border-right:1px solid #d5d5d5;display:flex;flex-direction:column}
.fields .col:last-child{border-right:none}
.fields .cell{height:26px;display:flex;align-items:center;gap:5px;padding-left:10px;font-family:"Poppins",sans-serif;font-size:11px;color:#333;white-space:nowrap}
.fields .row-even{background:var(--stripe)}
.fields .col.upper .cell{text-transform:uppercase;font-size:10.4px}
.tick{flex:none}
.footer{position:absolute;left:0;top:1123px;width:888px;height:77px}
.footer .phone{position:absolute;left:59px;top:18px;display:flex;align-items:center;gap:6px;font-family:"Poppins",sans-serif;font-weight:600;font-size:23px;color:var(--white)}
.footer .contact{position:absolute;top:20px;display:flex;align-items:center;gap:6px;font-family:"Poppins",sans-serif;font-size:15px;color:#222}
.icon-dot{width:28px;height:28px;border-radius:50%;background:var(--black);display:flex;align-items:center;justify-content:center}
</style>
</head>
<body>
<div class="page">

  <svg class="hero" width="888" height="122" viewBox="0 0 888 122" aria-hidden="true">
    <defs>
      <linearGradient id="heroTone" x1="0" y1="0" x2="1" y2="0">
        <stop offset="0" stop-color="#8a7a72"/>
        <stop offset=".35" stop-color="#b9b2ad"/>
        <stop offset=".6" stop-color="#3f6b2e"/>
        <stop offset="1" stop-color="#1f4a1c"/>
      </linearGradient>
    </defs>
    <rect x="0" y="118" width="888" height="3" fill="var(--red)"/>
    <polygon points="366,0 888,0 888,120 339,120" fill="url(#heroTone)" role="img" aria-label="Store associate in a red vest scanning shelf stock next to insect repellent cans"/>
    <polygon points="366,0 376,0 349,120 339,120" fill="var(--red)"/>
    <polygon points="880,0 888,0 888,20 860,120 850,120" fill="var(--red)"/>
  </svg>

  <div class="brand">
    <span class="brand-name">Birch Supply</span>
    <span class="brand-divider"></span>
    <span class="brand-unit"><span class="top">STORE SYSTEMS &amp;</span><span class="bottom">OPERATIONS</span></span>
  </div>

  <div class="title-band">
    <h1><span>ITEM CHANGE MANAGEMENT</span> FREQUENTLY ASKED QUESTIONS:</h1>
  </div>

  <!-- left column -->
  <section class="faq" style="left:59px;top:226px;width:430px">
    <div class="num">01</div>
    <div style="margin-left:46px;width:318px">
      <h2>Why do I even need to do item change management (ICM)?</h2>
      <p class="just">ICM simplifies and reduces the amount time and effort to manage the process of identifying and taking action against canceled, replacement, and reinstated items. Without ICM, the process of doing so is manual and laborious, error prone, and ultimately can result in taking lost sales. Contrarily, leveraging ICM (versus other manual approaches) typically saves stores between 8-12 hours per month, increase inventory accurateness, and improves operational effectiveness on the sales floor.</p>
    </div>
  </section>

  <section class="faq" style="left:59px;top:397px;width:430px">
    <div class="num">02</div>
    <div style="margin-left:49px;width:320px">
      <h2 style="padding-top:8px">How frequently should I be working ICM?</h2>
      <p>Weekly. This keeps the execution manageable and steady. Aim for consistency by performing ICM the same day each week.</p>
    </div>
  </section>

  <section class="faq" style="left:59px;top:473px;width:430px">
    <div class="num" style="top:14px">03</div>
    <div style="margin-left:50px;width:330px">
      <h2 style="padding-top:12px">My computer is ordering the replacement SKU when I'm not out of stock on the discontinued product. Why?</h2>
      <p>Confirm option configuration setting 9972 is set to option '2'. Doing so tells the system to order the new product only when the discontinued item falls to zero on hand.</p>
    </div>
  </section>

  <section class="faq" style="left:59px;top:597px;width:430px">
    <div class="num" style="top:13px">04</div>
    <div style="margin-left:48px;width:336px">
      <h2 style="padding-top:11px">I heard ICM merges product information. I've been using RCIN in Falcon for years to do that. Do I still need to use RCIN?</h2>
      <p>Managing items via ICM renders the need to do RCIN obsolete. ICM doesn't technically 'merge' items because doing so creates inventory issues as well as a loss of visibility to discontinued SKUs. ICM, on the other hand, copies over certain key information from the discontinued item to the new item, keeping the discontinued item intact to retain visibility and minimize long-term inventory accuracy issues.</p>
    </div>
  </section>

  <section class="faq" style="left:57px;top:781px;width:430px">
    <div class="num">05</div>
    <div style="margin-left:50px;width:330px">
      <h2 class="big" style="padding-top:2px">I'm in on ICM. How do I get started?</h2>
      <p>Great! Start by reviewing the Birch Way of Retailing Practice titled Item Change Management (Cancelled, Replacement, Temporary Closeout, and Reinstated Items) – Setup. Path: BIRCHNET &gt; About Birch Supply – Birch Way of Retailing &gt; BWOR Search: ICM.</p>
    </div>
  </section>

  <!-- right column -->
  <section class="faq" style="left:454px;top:231px;width:390px">
    <div class="num" style="left:0">06</div>
    <div style="margin-left:52px;width:330px">
      <h2>What in the world is the RICR report, and how does it relate to ICM?</h2>
      <p>RICR stands for 'Item Change Report' and prints after finalizing your work in ICM. Review it in the back office and on the sales floor as a means to update location codes and bin labels.</p>
    </div>
  </section>

  <section class="faq" style="left:454px;top:324px;width:390px">
    <div class="num">07</div>
    <div style="margin-left:52px;width:329px">
      <h2>Does ICM have any effect on my in-stock percentage measurement?</h2>
      <p class="just">Undoubtably. Stores regularly leveraging ICM weekly have shown to have a higher in-stock percentage than those that don't. ICM allows retailers to react faster and more effectively to items going away ensuring an effective plan is in place. Also, taking action against temporary out of stocks using ICM doesn't negatively impact your in-stock percentage.</p>
    </div>
  </section>

  <section class="faq" style="left:454px;top:462px;width:390px">
    <div class="num">08</div>
    <div style="margin-left:52px;width:332px">
      <h2 style="padding-top:1px">If I don't stock the SKU, will it appear in ICM?</h2>
      <p>No. Your ICM list is store specific, not a report of everything carried in the RSC. In other words, items you have not sold or purchased from the RSC in the last three years do not appear in the program for you to action.</p>
    </div>
  </section>

  <section class="faq" style="left:454px;top:536px;width:390px">
    <div class="num">09</div>
    <div style="margin-left:49px;width:333px">
      <h2>I have five stores in my chain. Can I review and execute ICM for all of them in one fell swoop?</h2>
      <p class="just">Sure. The reporting in ICM can be reviewed and executed centrally creating greater efficiencies when executing. Upon entering the BIRCHNET application, simply click the multi-store icon to select the stores you want to work on.</p>
    </div>
  </section>

  <section class="faq" style="left:454px;top:660px;width:390px">
    <div class="num">10</div>
    <div style="margin-left:49px;width:333px">
      <h2>I don't know if my SKUs are updating properly – how do I confirm?</h2>
      <p class="just">Compare the BIRCHNET PDF (available upon finalizing your work) to the Falcon RICR report to ensure all information has transmitted properly. If need be, you can also run the RICR report manually to serve as an audit tool. Within the ICM application, there is also an option to review previously finalized items for further investigation.</p>
    </div>
  </section>

  <section class="faq" style="left:455px;top:803px;width:390px">
    <div class="num">11</div>
    <div style="margin-left:46px;width:330px">
      <h2 class="big">Who do I contact with any further questions and support?</h2>
      <p style="margin-top:12px">Your field representative is always available to help answer questions. For further details about the program, you can also contact the Store Systems and Operations team.</p>
    </div>
  </section>

  <div class="table-title faq">
    <div class="num">11</div>
    <h2 class="big">I'm in on ICM. How do I get started?</h2>
  </div>

  <div class="fields">
    <div class="col upper">
      <div class="cell row-even"><svg class="tick" width="11" height="11" viewBox="0 0 12 12"><circle cx="6" cy="6" r="5" fill="none" stroke="#e31b3b" stroke-width="1"/><path d="M3.4 6.2l1.9 1.8 3.4-3.8" fill="none" stroke="#e31b3b" stroke-width="1.2"/></svg>Date Added</div>
      <div class="cell"><svg class="tick" width="11" height="11" viewBox="0 0 12 12"><circle cx="6" cy="6" r="5" fill="none" stroke="#e31b3b" stroke-width="1"/><path d="M3.4 6.2l1.9 1.8 3.4-3.8" fill="none" stroke="#e31b3b" stroke-width="1.2"/></svg>ROP Protect</div>
      <div class="cell row-even"><svg class="tick" width="11" height="11" viewBox="0 0 12 12"><circle cx="6" cy="6" r="5" fill="none" stroke="#e31b3b" stroke-width="1"/><path d="M3.4 6.2l1.9 1.8 3.4-3.8" fill="none" stroke="#e31b3b" stroke-width="1.2"/></svg>Order Point</div>
      <div class="cell"><svg class="tick" width="11" height="11" viewBox="0 0 12 12"><circle cx="6" cy="6" r="5" fill="none" stroke="#e31b3b" stroke-width="1"/><path d="M3.4 6.2l1.9 1.8 3.4-3.8" fill="none" stroke="#e31b3b" stroke-width="1.2"/></svg>Location Code(s)</div>
      <div class="cell row-even"><svg class="tick" width="11" height="11" viewBox="0 0 12 12"><circle cx="6" cy="6" r="5" fill="none" stroke="#e31b3b" stroke-width="1"/><path d="M3.4 6.2l1.9 1.8 3.4-3.8" fill="none" stroke="#e31b3b" stroke-width="1.2"/></svg>Expanded Promo History</div>
    </div>
    <div class="col">
      <div class="cell row-even"><svg class="tick" width="11" height="11" viewBox="0 0 12 12"><circle cx="6" cy="6" r="5" fill="none" stroke="#e31b3b" stroke-width="1"/><path d="M3.4 6.2l1.9 1.8 3.4-3.8" fill="none" stroke="#e31b3b" stroke-width="1.2"/></svg>Sales History</div>
      <div class="cell"><svg class="tick" width="11" height="11" viewBox="0 0 12 12"><circle cx="6" cy="6" r="5" fill="none" stroke="#e31b3b" stroke-width="1"/><path d="M3.4 6.2l1.9 1.8 3.4-3.8" fill="none" stroke="#e31b3b" stroke-width="1.2"/></svg>Max Stock Level</div>
      <div class="cell row-even"><svg class="tick" width="11" height="11" viewBox="0 0 12 12"><circle cx="6" cy="6" r="5" fill="none" stroke="#e31b3b" stroke-width="1"/><path d="M3.4 6.2l1.9 1.8 3.4-3.8" fill="none" stroke="#e31b3b" stroke-width="1.2"/></svg>Special Fees</div>
      <div class="cell"><svg class="tick" width="11" height="11" viewBox="0 0 12 12"><circle cx="6" cy="6" r="5" fill="none" stroke="#e31b3b" stroke-width="1"/><path d="M3.4 6.2l1.9 1.8 3.4-3.8" fill="none" stroke="#e31b3b" stroke-width="1.2"/></svg>Signature Required</div>
      <div class="cell row-even"><svg class="tick" width="11" height="11" viewBox="0 0 12 12"><circle cx="6" cy="6" r="5" fill="none" stroke="#e31b3b" stroke-width="1"/><path d="M3.4 6.2l1.9 1.8 3.4-3.8" fill="none" stroke="#e31b3b" stroke-width="1.2"/></svg>Popularity Code</div>
    </div>
    <div class="col">
      <div class="cell row-even"><svg class="tick" width="11" height="11" viewBox="0 0 12 12"><circle cx="6" cy="6" r="5" fill="none" stroke="#e31b3b" stroke-width="1"/><path d="M3.4 6.2l1.9 1.8 3.4-3.8" fill="none" stroke="#e31b3b" stroke-width="1.2"/></svg>PO Season Code</div>
      <div class="cell"><svg class="tick" width="11" height="11" viewBox="0 0 12 12"><circle cx="6" cy="6" r="5" fill="none" stroke="#e31b3b" stroke-width="1"/><path d="M3.4 6.2l1.9 1.8 3.4-3.8" fill="none" stroke="#e31b3b" stroke-width="1.2"/></svg>Tax Status</div>
      <div class="cell row-even"><svg class="tick" width="11" height="11" viewBox="0 0 12 12"><circle cx="6" cy="6" r="5" fill="none" stroke="#e31b3b" stroke-width="1"/><path d="M3.4 6.2l1.9 1.8 3.4-3.8" fill="none" stroke="#e31b3b" stroke-width="1.2"/></svg># of Labels</div>
      <div class="cell"><svg class="tick" width="11" height="11" viewBox="0 0 12 12"><circle cx="6" cy="6" r="5" fill="none" stroke="#e31b3b" stroke-width="1"/><path d="M3.4 6.2l1.9 1.8 3.4-3.8" fill="none" stroke="#e31b3b" stroke-width="1.2"/></svg>Expanded Sales History</div>
      <div class="cell row-even"></div>
    </div>
    <div class="col">
      <div class="cell row-even"><svg class="tick" width="11" height="11" viewBox="0 0 12 12"><circle cx="6" cy="6" r="5" fill="none" stroke="#e31b3b" stroke-width="1"/><path d="M3.4 6.2l1.9 1.8 3.4-3.8" fill="none" stroke="#e31b3b" stroke-width="1.2"/></svg>Tally</div>
      <div class="cell"><svg class="tick" width="11" height="11" viewBox="0 0 12 12"><circle cx="6" cy="6" r="5" fill="none" stroke="#e31b3b" stroke-width="1"/><path d="M3.4 6.2l1.9 1.8 3.4-3.8" fill="none" stroke="#e31b3b" stroke-width="1.2"/></svg>Loading Required</div>
      <div class="cell row-even"><svg class="tick" width="11" height="11" viewBox="0 0 12 12"><circle cx="6" cy="6" r="5" fill="none" stroke="#e31b3b" stroke-width="1"/><path d="M3.4 6.2l1.9 1.8 3.4-3.8" fill="none" stroke="#e31b3b" stroke-width="1.2"/></svg>Birch MSU's</div>
      <div class="cell"><svg class="tick" width="11" height="11" viewBox="0 0 12 12"><circle cx="6" cy="6" r="5" fill="none" stroke="#e31b3b" stroke-width="1"/><path d="M3.4 6.2l1.9 1.8 3.4-3.8" fill="none" stroke="#e31b3b" stroke-width="1.2"/></svg>CPP Discounts</div>
      <div class="cell row-even"></div>
    </div>
    <div class="col">
      <div class="cell row-even"><svg class="tick" width="11" height="11" viewBox="0 0 12 12"><circle cx="6" cy="6" r="5" fill="none" stroke="#e31b3b" stroke-width="1"/><path d="M3.4 6.2l1.9 1.8 3.4-3.8" fill="none" stroke="#e31b3b" stroke-width="1.2"/></svg>Discountable</div>
      <div class="cell"><svg class="tick" width="11" height="11" viewBox="0 0 12 12"><circle cx="6" cy="6" r="5" fill="none" stroke="#e31b3b" stroke-width="1"/><path d="M3.4 6.2l1.9 1.8 3.4-3.8" fill="none" stroke="#e31b3b" stroke-width="1.2"/></svg>User codes</div>
      <div class="cell row-even"><svg class="tick" width="11" height="11" viewBox="0 0 12 12"><circle cx="6" cy="6" r="5" fill="none" stroke="#e31b3b" stroke-width="1"/><path d="M3.4 6.2l1.9 1.8 3.4-3.8" fill="none" stroke="#e31b3b" stroke-width="1.2"/></svg>Promo History</div>
      <div class="cell"><svg class="tick" width="11" height="11" viewBox="0 0 12 12"><circle cx="6" cy="6" r="5" fill="none" stroke="#e31b3b" stroke-width="1"/><path d="M3.4 6.2l1.9 1.8 3.4-3.8" fill="none" stroke="#e31b3b" stroke-width="1.2"/></svg>Sells with SKU</div>
      <div class="cell row-even"></div>
    </div>
  </div>

  <footer class="footer">
    <svg width="888" height="77" viewBox="0 0 888 77" style="position:absolute;left:0;top:0" aria-hidden="true">
      <polygon points="0,0 282,0 310,68 888,68 888,77 0,77" fill="var(--red)"/>
      <polygon points="282,0 287,0 315,68 310,68" fill="var(--white)"/>
    </svg>
    <div class="phone">
      <svg width="28" height="28" viewBox="0 0 28 28"><circle cx="14" cy="14" r="13" fill="var(--white)"/><path d="M9.5 7.5l2.6 0 1.2 3.4-1.7 1.3c.8 1.9 2.3 3.4 4.2 4.2l1.3-1.7 3.4 1.2 0 2.6c0 .8-.7 1.5-1.5 1.5C13.3 20 8 14.7 8 9c0-.8.7-1.5 1.5-1.5z" fill="var(--red)"/></svg>
      555.014.2290
    </div>
    <div class="contact" style="left:326px">
      <span class="icon-dot"><svg width="14" height="12" viewBox="0 0 14 12"><rect x=".5" y="1" width="13" height="10" rx="1" fill="none" stroke="#fff"/><path d="M.8 1.5L7 6.5l6.2-5" fill="none" stroke="#fff"/></svg></span>
      storeoperations@birchsupply.com
    </div>
    <div class="contact" style="left:627px">
      <span class="icon-dot"><svg width="16" height="16" viewBox="0 0 16 16"><circle cx="8" cy="8" r="6.5" fill="none" stroke="#fff"/><ellipse cx="8" cy="8" rx="3" ry="6.5" fill="none" stroke="#fff"/><path d="M1.5 8h13M2.5 4.8h11M2.5 11.2h11" stroke="#fff" fill="none"/></svg></span>
      www.birchsupply.com
    </div>
  </footer>
</div>
</body>
</html>
```